Coach/consultant in conflict and challenge needs an enticing flyer

I need a double sided DL flyer design that will describe my work in helping people meet conflict and emotional challenge so they can learn and grow from these difficulties. I want to give a flavour of my style through fresh colours, repeated images used differently (the spiral), and a sense of positivity around conflict and difficulty. I want to attract people who are keen to do things differently and want to engage with creative processes rather than getting stuck in familiar patterns. My work is creative and often includes use of story, images and fables, so I want to convey that as well. I also place the work in a spiritual context, but grounded in practicality so I don't want it to seem New Age or flakey. I want something that seems innovative, professional and intriguing. I've included a sample of something I mocked up in word and also a copy of a flyer for Marla Quennet's Ember Gathering that inspired me to get a DL flyer. I want the design to communicate trust and transformation and engaging with fresh ways of doing things by moving past old habits

Target Market(s)

Mid 30s plus women and men who want to change their approach to conflict and emotional difficulties and are willing to take the creative and challenging journey to do that

Industry/Entity Type

Learn

Colors
acd136
00a990

Requirements
Must have
• a shift in the use of the spiral image,
• use of image of me (Norah)
• bright fresh colours olours that represent growth and transformation--I've suggested lime green as it suggests a sense of growth
• easy to read text
Nice to have
• Interesting non-traditional fonts perhaps text in a contemporary sans serif and another brush script font (like the Ember Gathering example)
• bleed to the edge and run off the page images or text
Should not have
• anything that represents too much tradition or stuckness

```html
<!DOCTYPE html>
<html lang="en">
<head>
<meta charset="utf-8">
<title>Norah Ashgrove – DL Flyer</title>
<link rel="stylesheet" href="https://fonts.googleapis.com/css2?family=Permanent+Marker&family=Saira:ital,wght@0,300;0,400;1,300;1,400&display=swap">
<style>
  :root{
    --page:#e8e5e0;
    --lime:#acd136;
    --lime-soft:#b8da4a;
    --brown:#6e4a33;
    --ink:#2f2a24;
    --white:#ffffff;
    --orange:#e0612a;
  }
  *{margin:0;padding:0;box-sizing:border-box}
  html,body{width:1200px;height:1200px;overflow:hidden;background:var(--page)}
  body{position:relative;font-family:"Saira",sans-serif;color:var(--ink)}

  .flyer-side{position:absolute;left:74px;width:1052px;height:496px;background:var(--lime);overflow:hidden}
  .flyer-front{top:98px}
  .flyer-back{top:617px}

  .swirl-glow{position:absolute;border-radius:50%;border:70px solid var(--lime-soft);opacity:.55}

  .brush-name{font-family:"Permanent Marker",sans-serif;font-weight:400;color:var(--brown);line-height:1;white-space:nowrap}

  /* front */
  .spiral-art{position:absolute;left:74px;top:134px;width:280px;height:260px;border-radius:50%;
    background:radial-gradient(circle at 50% 50%,rgba(122,78,44,.95) 0%,rgba(138,90,46,.8) 45%,rgba(172,209,54,0) 72%)}
  .front-name{position:absolute;left:402px;top:100px;font-size:44px}
  .front-tags{position:absolute;left:378px;top:150px;font-size:29px;font-weight:400;color:var(--white);white-space:nowrap}
  .front-tags span{margin-right:22px}
  .front-lead{position:absolute;left:408px;top:203px;width:570px;font-size:22.5px;line-height:27.5px;color:var(--white);font-weight:400}
  .front-bio{position:absolute;left:506px;top:366px;width:480px;font-size:16.5px;line-height:21px;font-style:italic;font-weight:300;color:var(--ink)}
  .front-bio strong{font-weight:400}

  /* back */
  .back-copy{position:absolute;left:71px;top:53px;width:620px;font-size:18.5px;line-height:23.4px;font-weight:300;color:var(--ink)}
  .back-name{position:absolute;left:71px;top:270px;font-size:26px}
  .back-creds{position:absolute;left:72px;top:303px;font-size:12.5px;font-weight:400;color:var(--ink)}
  .portrait{position:absolute;left:790px;top:59px;width:262px;height:437px;border-radius:48% 48% 0 0/34% 34% 0 0;
    background:linear-gradient(180deg,#8c8277 0%,#c9a58a 40%,var(--orange) 62%,#d4521e 100%)}
  .service-list{position:absolute;z-index:2;left:498px;top:232px;list-style:none;font-family:"Permanent Marker",sans-serif;font-size:25px;line-height:31px;color:var(--white);white-space:nowrap}
  .service-list li::before{content:"•";font-family:"Saira",sans-serif;font-size:16px;margin-right:8px;vertical-align:middle}
  .contact-row{position:absolute;left:68px;display:flex;align-items:center;font-size:19.5px;color:var(--ink)}
  .contact-row.phones{top:370px}
  .contact-row.web{top:410px}
  .icon{width:33px;height:33px;flex:none;margin-right:12px}
  .divider{width:2px;height:30px;background:var(--ink);margin:0 14px 0 18px}
  .gap{width:30px}
  .abn{position:absolute;left:114px;top:451px;font-size:9px;color:var(--ink)}
  .ghost-name{position:absolute;z-index:1;left:520px;top:444px;font-size:50px;color:var(--white);opacity:.2}
</style>
</head>
<body>

<section class="flyer-side flyer-front">
  <div class="swirl-glow" style="left:-60px;top:-120px;width:820px;height:820px"></div>
  <div class="spiral-art" role="img" aria-label="Brown brush-painted spiral artwork"></div>
  <h1 class="brush-name front-name">NORAH ASHGROVE</h1>
  <p class="front-tags"><span># COURAGE</span><span># LISTENING</span># CREATIVITY</p>
  <p class="front-lead">Challenge, change and conflict are a natural part of life. When we greet them with courage, and listen to what they tell us, we grow in wisdom, resilience and creativity.</p>
  <p class="front-bio"><strong>Norah Ashgrove</strong> is a coach, educator and mediator. She works with people who want to harvest the fruits of challenge and conflict so they live life differently.</p>
</section>

<section class="flyer-side flyer-back">
  <div class="swirl-glow" style="left:560px;top:120px;width:640px;height:640px"></div>
  <p class="back-copy">Consult with Norah to address challenges in your life, relationship, group or organisation. Through listening, conversation and creative processes, you will discover what your challenge is asking of you. Norah Ashgrove is a skilled facilitator who works to shift people’s responses from reactivity to creativity.<br>With many years’ experience in coaching and mentorship, mediation and narrative processes, Norah supports you to uncover unique responses to difficult situations.</p>

  <h2 class="brush-name back-name">NORAH ASHGROVE</h2>
  <p class="back-creds">PhD, MCR, BAppSci, DipHum, AssDipEd</p>

  <div class="portrait" role="img" aria-label="Portrait photograph of Norah in an orange knitted top"></div>

  <ul class="service-list">
    <li>CONSULTATIONS</li>
    <li>WORKSHOPS</li>
    <li>SPEAKING</li>
    <li>ARTICLES</li>
  </ul>

  <div class="contact-row phones">
    <svg class="icon" viewBox="0 0 32 32" aria-hidden="true"><circle cx="16" cy="16" r="16" fill="#6e4a33"/><path d="M11 8l3 3-1.6 2.4c1 2.2 2.5 3.7 4.6 4.6L19.4 16.4l3 3-2 2.6C14 21.5 10.5 18 10 11.6z" fill="#fff"/></svg>
    <span>0400 555 218 (m)</span>
    <span class="divider"></span>
    <span>+61 3 9000 4417 (h)</span>
  </div>
  <div class="contact-row web">
    <svg class="icon" viewBox="0 0 32 32" aria-hidden="true"><circle cx="16" cy="16" r="16" fill="#6e4a33"/><rect x="8" y="10" width="16" height="12" fill="none" stroke="#fff" stroke-width="1.6"/><path d="M8 10l8 7 8-7M8 22l6-6M24 22l-6-6" fill="none" stroke="#fff" stroke-width="1.4"/></svg>
    <span>norah@norahashgrove.com</span>
    <span class="gap"></span>
    <svg class="icon" viewBox="0 0 32 32" aria-hidden="true"><circle cx="16" cy="16" r="16" fill="#6e4a33"/><g fill="none" stroke="#fff" stroke-width="1.4"><circle cx="16" cy="16" r="8"/><ellipse cx="16" cy="16" rx="3.5" ry="8"/><path d="M8 16h16M9.5 12h13M9.5 20h13"/></g></svg>
    <span>norahashgrove.com</span>
  </div>
  <p class="abn">ABN 12 345 678 90</p>

  <p class="brush-name ghost-name">NORAH ASHGROVE</p>
</section>

</body>
</html>
```